Soccer (Football) travel website

I need a responsive 1-page website design for a vacation/trip review website, plus a basic logo. The site's name is GlobeKickJourneys.com.

A site I have in mind is VoyagePanel.com:

https://www.voyagepanel.com/sailto/sailroutes.cfm?port=149&startDate=2019-08

Target Market(s)

Landing page used to attract people after they've clicked on an advertisement

Industry/Entity Type

Travel

Logo Text

GlobeKickJourneys.com

Number of Pages Required

1 page

Font styles to use
Sans Serif

Colors

Designer to choose colors to be used in the design.

Requirements
Must have
• A header that takes up very little vertical space.
• I've attached one file. This is what the content will consist of in the center of the site: a photo of a stadium with some description text below it.
Nice to have
• Needs to have a simple nav plus links for social media and newsletter

```html
<!DOCTYPE html>
<html lang="en">
<head>
<meta charset="utf-8">
<title>GlobeKickJourneys – Find Your Trip</title>
<link href="https://fonts.googleapis.com/css2?family=Montserrat:wght@400;500;600;700&display=swap" rel="stylesheet">
<style>
:root{
  --red:#d93a2f;
  --red-dark:#c12f25;
  --ink:#2b2b2b;
  --muted:#555;
  --line:#e3e3e3;
  --white:#fff;
  --grey-band:#6a6a6c;
  --grey-foot:#4d4d4f;
  --btn-grey:#cfcfcf;
}
*{box-sizing:border-box;margin:0;padding:0}
html,body{width:1200px;height:2247px;overflow:hidden}
body{font-family:"Montserrat",Arial,sans-serif;color:var(--ink);background:var(--white);position:relative}
.abs{position:absolute}

/* header */
.site-header{position:absolute;left:0;top:0;width:1200px;height:37px;background:var(--red)}
.brand{left:195px;top:10px;font-size:13.5px;font-weight:600;color:var(--white);letter-spacing:-.2px;white-space:nowrap}
.main-nav{left:352px;top:12px;display:flex;gap:22px;font-size:10.5px;font-weight:500;color:var(--white);white-space:nowrap}
.main-nav .caret{font-size:8px;margin-left:4px}
.search{left:504px;top:0;width:291px;height:37px;background:var(--white);display:flex;align-items:center;padding-left:14px;gap:12px;font-size:10px;color:#999;white-space:nowrap}
.tools{left:795px;top:0;display:flex}
.tool{width:48px;height:37px;display:flex;flex-direction:column;align-items:center;justify-content:center;gap:3px;color:var(--white);font-size:6.5px;font-weight:600;border-left:1px solid rgba(255,255,255,.2);white-space:nowrap}

/* hero */
.hero{left:0;top:37px;width:1200px;height:393px;background:linear-gradient(180deg,#e9ecea 0%,#b9b8a9 30%,#5f7a3a 55%,#6d7a44 68%,#a59a6b 85%,#8c8a6a 100%)}
.hero h1{position:absolute;left:0;width:1200px;top:209px;text-align:center;font-size:30px;font-weight:700;color:var(--white)}
.hero-tabs{position:absolute;left:0;width:1200px;top:258px;display:flex;justify-content:center;gap:20px;font-size:9.5px;font-weight:600;color:var(--white)}
.hero-tabs span::before{content:"";display:inline-block;width:7px;height:7px;border-radius:50%;background:var(--white);margin-right:6px;vertical-align:middle}
.select{position:absolute;top:291px;height:36px;background:var(--white);font-size:10px;color:#999;padding:12px 12px;border-radius:2px}
.select::after{content:"";position:absolute;right:12px;top:16px;border:4px solid transparent;border-top-color:#555}
.btn{display:inline-flex;align-items:center;justify-content:center;gap:8px;background:var(--red);color:var(--white);font-size:10px;font-weight:500;border-radius:2px;white-space:nowrap}
.hero .btn{position:absolute;left:722px;top:291px;width:99px;height:36px}

/* section heads */
.section-title{font-size:19px;font-weight:500;color:#333}
.pager{display:flex;gap:4px}
.pager span{width:19px;height:18px;border-radius:2px;background:var(--btn-grey);display:flex;align-items:center;justify-content:center;color:#777;font-size:8px}
.pager span.on{background:var(--red);color:var(--white)}

/* how to */
.media{background:linear-gradient(135deg,#7a8a5a,#c9a06b 45%,#f3d8a7 60%,#6b5a50)}
.lead-img{left:195px;top:517px;width:390px;height:193px;border-radius:2px}
.lead-title{left:195px;top:727px;font-size:13px;font-weight:700}
.lead-text{left:195px;top:750px;font-size:9.5px;color:var(--muted)}
.item{position:absolute;display:flex;gap:18px;width:390px}
.thumb{width:102px;height:74px;flex:none}
.item h3{font-size:13px;font-weight:500;margin-top:4px;margin-bottom:12px}
.item p{font-size:9px;line-height:13px;color:var(--muted);width:270px}
.dest .thumb{background:linear-gradient(160deg,#8fc9c4 0%,#a9c96a 45%,#5e8a2e 100%)}

/* dark band */
.numbers{left:0;top:843px;width:1200px;height:357px;background:radial-gradient(circle at 330px 60px,#3a1512 0,#1b0f0e 120px,transparent 121px),linear-gradient(180deg,#141414 0%,#23272c 30%,#35404a 55%,#3b4a2e 70%,#2a3a1a 100%)}
.numbers h2{position:absolute;left:195px;top:46px;font-size:19px;font-weight:500;color:var(--red)}
.num-list{position:absolute;left:195px;top:82px;width:505px;list-style:none}
.num-list li{height:33.7px;display:flex;align-items:center;border-bottom:1px solid rgba(255,255,255,.12);font-size:10px;color:var(--white);white-space:nowrap}
.num-list li:last-child{border-bottom:none}
.num-list b{font-size:13px;font-weight:700;margin-right:5px}
.num-list i{font-style:normal;color:var(--red);margin-left:8px}
.poll{position:absolute;left:743px;top:39px;width:262px;height:226px;background:var(--white);padding:18px 18px}
.poll h4{font-size:10.5px;font-weight:700;margin-bottom:12px}
.poll h3{font-size:19px;font-weight:500;color:var(--red);line-height:23px;margin-bottom:18px}
.poll label{display:flex;align-items:center;gap:9px;font-size:10px;color:var(--muted);height:22.5px;white-space:nowrap}
.poll label span{width:9px;height:9px;border-radius:50%;border:1px solid #bbb}
.poll label span.on{border:3px solid #555}
.numbers .btn{position:absolute;left:741px;top:283px;width:63px;height:35px}

/* cta band */
.cta-band{left:0;top:1613px;width:1200px;height:315px;background:linear-gradient(180deg,#d9d2c4 0%,#ead8ae 35%,#d9a26b 70%,#8a6a52 100%)}
.card{position:absolute;top:45px;width:263px;height:225px;background:var(--white);text-align:center;padding-top:25px}
.card svg{display:block;margin:0 auto 14px}
.card h4{font-size:10.5px;font-weight:700;margin-bottom:16px}
.card h3{font-size:17.5px;font-weight:500;color:var(--red);line-height:23px;margin-bottom:16px;white-space:nowrap}
.card .btn{height:35px;padding:0 16px}

/* newsletter */
.newsletter{left:0;top:1928px;width:1200px;height:176px;background:var(--grey-band);text-align:center;color:var(--white)}
.newsletter h4{margin-top:46px;font-size:11px;font-weight:700}
.newsletter p{font-size:10.5px;margin-top:6px}
.subscribe{display:flex;justify-content:center;gap:6px;margin-top:15px}
.subscribe .field{width:209px;height:35px;background:var(--white);color:#999;font-size:10px;text-align:left;padding:12px 18px}
.subscribe .btn{width:75px;height:35px}

/* footer */
.site-footer{left:0;top:2104px;width:1200px;height:143px;background:var(--grey-foot);color:#ddd}
.site-footer .brand{top:44px}
.foot-col{position:absolute;top:44px;list-style:none;font-size:8.5px;line-height:14.5px;white-space:nowrap}
.copy{position:absolute;right:195px;top:45px;font-size:8.5px;white-space:nowrap}
</style>
</head>
<body>

<header class="site-header">
  <div class="abs brand">globekickjourneys</div>
  <nav class="abs main-nav"><span>Research<span class="caret">▼</span></span><span>Find a Trip</span></nav>
  <div class="abs search">
    <svg width="12" height="12" viewBox="0 0 12 12"><circle cx="5" cy="5" r="3.8" fill="none" stroke="#d93a2f" stroke-width="1.6"/><path d="M8 8l3 3" stroke="#d93a2f" stroke-width="1.6"/></svg>
    Search Stadiums, Destinations, etc.
  </div>
  <div class="abs tools">
    <div class="tool"><svg width="12" height="12" viewBox="0 0 12 12"><path d="M1 11l1-3 6-6 2 2-6 6z" fill="#fff"/></svg>Write Review</div>
    <div class="tool"><svg width="13" height="12" viewBox="0 0 13 12"><ellipse cx="5" cy="5" rx="5" ry="4" fill="#fff"/><ellipse cx="9" cy="7" rx="4" ry="3.3" fill="#fff" stroke="#d93a2f"/></svg>Boards</div>
    <div class="tool"><svg width="11" height="12" viewBox="0 0 11 12"><circle cx="5.5" cy="3.5" r="3" fill="#fff"/><path d="M0 12c0-4 2.5-5 5.5-5s5.5 1 5.5 5z" fill="#fff"/></svg>Login</div>
    <div class="tool"><svg width="12" height="11" viewBox="0 0 12 11"><path d="M6 11L1 6a3 3 0 015-4 3 3 0 015 4z" fill="#fff"/></svg>Saved</div>
  </div>
</header>

<section class="abs hero" role="img" aria-label="Lakeside park with trees and a mountain reflected in calm water at sunset">
  <h1>Find Your GlobeKickJourneys</h1>
  <div class="hero-tabs"><span>Find a Trip</span><span>Stadiums</span><span>Destinations</span><span>Find Your Roll Call</span></div>
  <div class="select" style="left:391px;width:157px">Any Destination</div>
  <div class="select" style="left:557px;width:159px">Any Month</div>
  <a class="btn">Find a Trip <span>›</span></a>
</section>

<section class="how-to">
  <h2 class="abs section-title" style="left:195px;top:465px">How to GlobeKickJourneys</h2>
  <div class="abs pager" style="left:963px;top:467px"><span>‹</span><span class="on">›</span></div>
  <div class="abs lead-img media" role="img" aria-label="Traveller with a hat and map sitting by railway tracks"></div>
  <h3 class="abs lead-title">Lorem Ipsum is simply dummy text of the printing!</h3>
  <p class="abs lead-text">Lorem Ipsum is simply dummy text of the printing and typesetting industry.</p>
  <div class="item" style="left:616px;top:517px"><div class="thumb media" role="img" aria-label="Traveller by railway tracks"></div><div><h3>Lorem Ipsum is simply</h3><p>Lorem Ipsum has been the industry's standard dummy text ever since the 1500s, when an unknown.</p></div></div>
  <div class="item" style="left:616px;top:600px"><div class="thumb media" role="img" aria-label="Traveller by railway tracks"></div><div><h3>Lorem Ipsum is simply</h3><p>Lorem Ipsum has been the industry's standard dummy text ever since the 1500s, when an unknown.</p></div></div>
  <div class="item" style="left:616px;top:684px"><div class="thumb media" role="img" aria-label="Traveller by railway tracks"></div><div><h3>Lorem Ipsum is simply</h3><p>Lorem Ipsum has been the industry's standard dummy text ever since the 1500s, when an unknown.</p></div></div>
</section>

<section class="abs numbers" role="img" aria-label="Hot air balloons over a field at dusk">
  <h2>GlobeKickJourneys Number</h2>
  <ul class="num-list">
    <li><b>Lorem Ipsum:</b> Simply dummy text <i>›</i></li>
    <li><b>Lorem Ipsum:</b> Simply dummy text of the printing! <i>›</i></li>
    <li><b>Lorem Ipsum:</b> Simply dummy text of the printing! <i>›</i></li>
    <li><b>Lorem Ipsum:</b> Simply dummy text of the. <i>›</i></li>
    <li><b>Lorem Ipsum:</b> Simply dummy text of the printing! <i>›</i></li>
    <li><b>Lorem Ipsum:</b> Simply dummy text <i>›</i></li>
    <li><b>Lorem Ipsum:</b> Simply dummy text of the printing! <i>›</i></li>
  </ul>
  <div class="poll">
    <h4>Today's Poll</h4>
    <h3>Would you GlobeKickJourneys season?</h3>
    <label><span class="on"></span>Yes, I'm already booked.</label>
    <label><span></span>Yes, I would.</label>
    <label><span></span>Maybe, if I could get a good deal.</label>
    <label><span></span>No, I wouldn't.</label>
  </div>
  <a class="btn">Vote <span>›</span></a>
</section>

<section class="dest">
  <h2 class="abs section-title" style="left:195px;top:1236px">Featured Destinations</h2>
  <div class="abs pager" style="left:963px;top:1238px"><span>‹</span><span class="on">›</span></div>
  <div class="item" style="left:195px;top:1285px"><div class="thumb" role="img" aria-label="Green terraced hillside"></div><div><h3>Lorem Ipsum is simply</h3><p>Lorem Ipsum has been the industry's standard dummy text ever since the 1500s, when an unknown.</p></div></div>
  <div class="item" style="left:616px;top:1285px"><div class="thumb" role="img" aria-label="Green terraced hillside"></div><div><h3>Lorem Ipsum is simply</h3><p>Lorem Ipsum has been the industry's standard dummy text ever since the 1500s, when an unknown.</p></div></div>
  <div class="item" style="left:195px;top:1369px"><div class="thumb" role="img" aria-label="Green terraced hillside"></div><div><h3>Lorem Ipsum is simply</h3><p>Lorem Ipsum has been the industry's standard dummy text ever since the 1500s, when an unknown.</p></div></div>
  <div class="item" style="left:616px;top:1369px"><div class="thumb" role="img" aria-label="Green terraced hillside"></div><div><h3>Lorem Ipsum is simply</h3><p>Lorem Ipsum has been the industry's standard dummy text ever since the 1500s, when an unknown.</p></div></div>
  <div class="item" style="left:195px;top:1453px"><div class="thumb" role="img" aria-label="Green terraced hillside"></div><div><h3>Lorem Ipsum is simply</h3><p>Lorem Ipsum has been the industry's standard dummy text ever since the 1500s, when an unknown.</p></div></div>
  <div class="item" style="left:616px;top:1453px"><div class="thumb" role="img" aria-label="Green terraced hillside"></div><div><h3>Lorem Ipsum is simply</h3><p>Lorem Ipsum has been the industry's standard dummy text ever since the 1500s, when an unknown.</p></div></div>
</section>

<section class="abs cta-band" role="img" aria-label="Aircraft wing above clouds at sunset">
  <div class="card" style="left:195px">
    <svg width="32" height="32" viewBox="0 0 32 32"><path d="M4 28l2-7L22 5l5 5L11 26z" fill="#d93a2f"/><path d="M20 7l5 5" stroke="#fff" stroke-width="1.5"/></svg>
    <h4>Write a Review</h4>
    <h3>Share your experience<br>with other travellers</h3>
    <a class="btn">Write a Review <span>›</span></a>
  </div>
  <div class="card" style="left:469px">
    <svg width="40" height="32" viewBox="0 0 40 32"><circle cx="8" cy="12" r="4" fill="#d93a2f"/><circle cx="32" cy="12" r="4" fill="#d93a2f"/><circle cx="20" cy="9" r="5.5" fill="#d93a2f"/><path d="M1 26c0-6 3-8 7-8s7 2 7 8zM25 26c0-6 3-8 7-8s7 2 7 8zM11 26c0-8 4-10 9-10s9 2 9 10z" fill="#d93a2f"/></svg>
    <h4>Join Our Community</h4>
    <h3>Become a member to<br>access our boards</h3>
    <a class="btn">Community <span>›</span></a>
  </div>
  <div class="card" style="left:743px">
    <svg width="36" height="32" viewBox="0 0 36 32"><path d="M3 11h6l9-7v24l-9-7H3z" fill="#d93a2f"/><path d="M23 11a6 6 0 010 10M27 7a11 11 0 010 18M31 3a16 16 0 010 26" fill="none" stroke="#d93a2f" stroke-width="2"/></svg>
    <h4>Already Booked?</h4>
    <h3>Get to know who you'll<br>be travelling with</h3>
    <a class="btn">Find Your Roll Call <span>›</span></a>
  </div>
</section>

<section class="abs newsletter">
  <h4>Want to globekickjourneys smarter?</h4>
  <p>Get expert advice, insider tips and more.</p>
  <div class="subscribe"><div class="field">Enter Your e-mail Here</div><a class="btn">Subscribe</a></div>
</section>

<footer class="abs site-footer">
  <div class="abs brand">globekickjourneys</div>
  <ul class="foot-col" style="left:354px"><li>About Us</li><li>Privacy</li><li>Terms of Use</li><li>Site Map</li></ul>
  <ul class="foot-col" style="left:440px"><li>GlobeKickJourneys Destinations</li><li>GlobeKickJourneys Reviews</li><li>First Time GlobeKickJourneys</li><li>Find a GlobeKickJourneys</li></ul>
  <ul class="foot-col" style="left:599px"><li>GlobeKickJourneys Deals</li><li>Last Minute GlobeKickJourneys Deals</li><li>Caribbean GlobeKickJourneys Deals</li><li>Alaska GlobeKickJourneys Deals</li></ul>
  <p class="copy">© 2018, GlobeKickJourneys. All Rights Reserved</p>
</footer>

</body>
</html>
```